Morvella! Poster

I need a poster for an event to be staged in Gibraltar called Morvella!
Morvella! is a food festival and street party that celebrates GIbraltar's multicultural and colour community. The event has a tagline "Flavours of the Open Table".
I am looking for a poster which captures the spirit of the event without being too obvious.
Updates

Because this event is rapidly approaching I would like to settle the design for the poster as soon as possible, so the earlier you post the better
thanks

I am trying to avoid a poster that looks too similar to last year's.
Red and White are Gibraltar's national colours and I would like to feature them in the design.
Morvella! the name needs to be in Clarendon! (bold) with tight character spacing

Target Market(s)

Target market are the people of Gibraltar - Gibraltar is a british colony in southern Spain, population 30,000 - Gibraltarians are of British, Spanish, Italian (Genoa), Portugese and Moroccan extraction. Gibraltar also has large Hindu, Jewish and Moroccan Communities.

Industry/Entity Type

Events

Requirements
Must have
• Initially I am looking for an A2 design - we will use the same design themes for the website and also base a 120cm x 90cm banner on the design.
• Must have t
• "BrightLanternShows.com" "Morvella!" , "Flavours of the Open Table", Friday June 19th 2009, Tollgate Plaza, Starts 21.00 hrs Finishes 0100 hrs, Free Entry, Everyone Welcome, Firework and Laser Display at 22.30 hrs
• My company logo, Office of Heritage Summer Fair Logo
• Title must use Clarendon font
Nice to have
• Could be a photo or an illustration nothing that too obviously reflects the theme, doesn''t need to have all or anymore than one of the main Gibraltarian cultures
Should not have
• picture of the ROck of Gibaltar, Money, bad photography in particular bad food photography, just a picture of some food

```html
<!DOCTYPE html>
<html lang="en">
<head>
<meta charset="utf-8">
<title>Morvella! – Flavours of the Open Table</title>
<link href="https://fonts.googleapis.com/css2?family=Coustard:wght@400;900&family=Roboto+Condensed:wght@700&display=swap" rel="stylesheet">
<style>
  :root {
    --frame: #d35a2e;
    --orange: #ff7f00;
    --maroon: #a1222f;
    --sky: #12b4f5;
    --navy: #1c0a55;
    --white: #ffffff;
  }
  * { margin: 0; padding: 0; box-sizing: border-box; }
  html, body { width: 848px; height: 1200px; overflow: hidden; background: var(--frame); }
  .poster {
    position: relative;
    width: 848px;
    height: 1200px;
    background: var(--frame);
    overflow: hidden;
  }
  .tile-mosaic {
    position: absolute;
    left: 16px; top: 14px;
    width: 817px; height: 677px;
    background: var(--white);
    display: block;
  }
  .tile-mosaic .t-orange { fill: var(--orange); }
  .tile-mosaic .t-maroon { fill: var(--maroon); }
  .tile-mosaic .t-sky { fill: var(--sky); }
  .tile-mosaic .t-navy { fill: var(--navy); }
  .title-box {
    position: absolute;
    left: 16px; top: 705px;
    width: 817px; height: 139px;
    background: var(--white);
    display: flex;
    align-items: center;
    justify-content: center;
  }
  .event-name {
    font-family: "Coustard", "Clarendon", serif;
    font-weight: 900;
    font-size: 150px;
    line-height: 1;
    letter-spacing: -4px;
    color: var(--maroon);
    margin-top: 6px;
  }
  .info-band {
    position: absolute;
    left: 0; top: 851px;
    width: 848px; height: 349px;
    background: var(--orange);
  }
  .tagline {
    position: absolute;
    left: 0; top: 0;
    width: 100%;
    text-align: center;
    font-family: "Coustard", serif;
    font-weight: 900;
    font-size: 55px;
    line-height: 1.1;
    letter-spacing: -2px;
    color: var(--white);
    white-space: nowrap;
  }
  .details {
    position: absolute;
    left: 112px; top: 77px;
    width: 623px; height: 195px;
    background: var(--maroon);
    border-radius: 14px;
    display: flex;
    flex-direction: column;
    align-items: center;
    justify-content: center;
    font-family: "Roboto Condensed", "Arial Narrow", sans-serif;
    font-weight: 700;
    font-size: 70px;
    line-height: 62px;
    letter-spacing: -1.5px;
    color: var(--white);
  }
  .details span { display: block; white-space: nowrap; }
  .welcome {
    position: absolute;
    left: 0; top: 281px;
    width: 100%;
    text-align: center;
    font-family: "Roboto Condensed", "Arial Narrow", sans-serif;
    font-weight: 700;
    font-size: 30px;
    letter-spacing: -1.4px;
    color: var(--white);
    white-space: nowrap;
  }
  .promoter {
    position: absolute;
    left: 0; top: 328px;
    width: 100%;
    text-align: center;
    font-family: "Coustard", serif;
    font-size: 15px;
    letter-spacing: 2px;
    color: var(--white);
  }
</style>
</head>
<body>
  <main class="poster">
    <svg class="tile-mosaic" viewBox="22 20 1146 950" preserveAspectRatio="none" role="img" aria-label="Mosaic of coloured kitchen tiles: fish, salt shakers, whisks, wine glasses, cutlery, spring onions, garlic and strawberries">
      <g>
        <rect class="t-orange" x="40" y="10" width="115" height="100" rx="22"/>
        <rect class="t-orange" x="170" y="10" width="90" height="95" rx="22"/>
        <rect class="t-maroon" x="290" y="10" width="265" height="75" rx="22"/>
        <rect class="t-orange" x="580" y="30" width="110" height="170" rx="22"/>
        <rect class="t-sky" x="710" y="10" width="280" height="50" rx="22"/>
        <rect class="t-sky" x="1020" y="10" width="150" height="85" rx="22"/>
        <rect class="t-sky" x="45" y="120" width="280" height="90" rx="22"/>
        <rect class="t-sky" x="340" y="115" width="220" height="100" rx="22"/>
        <rect class="t-maroon" x="708" y="92" width="90" height="100" rx="22"/>
        <rect class="t-sky" x="815" y="98" width="280" height="95" rx="22"/>
        <rect class="t-orange" x="1120" y="115" width="60" height="170" rx="22"/>
        <rect class="t-sky" x="10" y="255" width="120" height="90" rx="22"/>
        <rect class="t-navy" x="143" y="243" width="280" height="100" rx="22"/>
        <rect class="t-orange" x="432" y="265" width="115" height="175" rx="22"/>
        <rect class="t-sky" x="565" y="215" width="290" height="90" rx="22"/>
        <rect class="t-maroon" x="905" y="215" width="180" height="110" rx="22"/>
        <rect class="t-orange" x="570" y="320" width="80" height="100" rx="22"/>
        <rect class="t-sky" x="1095" y="315" width="85" height="90" rx="22"/>
        <rect class="t-maroon" x="10" y="365" width="195" height="115" rx="22"/>
        <rect class="t-sky" x="218" y="365" width="205" height="125" rx="22"/>
        <rect class="t-maroon" x="680" y="330" width="270" height="100" rx="22"/>
        <rect class="t-orange" x="962" y="365" width="105" height="170" rx="22"/>
        <rect class="t-maroon" x="1098" y="430" width="80" height="120" rx="22"/>
        <rect class="t-sky" x="418" y="460" width="295" height="110" rx="22"/>
        <rect class="t-sky" x="725" y="455" width="220" height="125" rx="22"/>
        <rect class="t-maroon" x="10" y="495" width="268" height="105" rx="22"/>
        <rect class="t-orange" x="290" y="515" width="115" height="175" rx="22"/>
        <rect class="t-maroon" x="420" y="585" width="90" height="115" rx="22"/>
        <rect class="t-sky" x="525" y="590" width="280" height="95" rx="22"/>
        <rect class="t-maroon" x="990" y="550" width="190" height="105" rx="22"/>
        <rect class="t-sky" x="52" y="610" width="225" height="120" rx="22"/>
        <rect class="t-orange" x="825" y="600" width="120" height="170" rx="22"/>
        <rect class="t-orange" x="960" y="660" width="85" height="110" rx="22"/>
        <rect class="t-maroon" x="1075" y="675" width="105" height="110" rx="22"/>
        <rect class="t-sky" x="285" y="710" width="290" height="90" rx="22"/>
        <rect class="t-maroon" x="620" y="705" width="180" height="120" rx="22"/>
        <rect class="t-orange" x="140" y="745" width="110" height="170" rx="22"/>
        <rect class="t-sky" x="10" y="750" width="125" height="80" rx="22"/>
        <rect class="t-orange" x="285" y="815" width="95" height="100" rx="22"/>
        <rect class="t-maroon" x="390" y="825" width="270" height="95" rx="22"/>
        <rect class="t-sky" x="800" y="790" width="305" height="110" rx="22"/>
        <rect class="t-sky" x="1110" y="800" width="70" height="140" rx="22"/>
        <rect class="t-maroon" x="10" y="850" width="100" height="115" rx="22"/>
        <rect class="t-orange" x="675" y="850" width="115" height="130" rx="22"/>
        <rect class="t-maroon" x="805" y="915" width="85" height="70" rx="22"/>
        <rect class="t-sky" x="920" y="935" width="250" height="50" rx="22"/>
        <rect class="t-sky" x="140" y="955" width="280" height="40" rx="22"/>
        <rect class="t-sky" x="455" y="955" width="200" height="40" rx="22"/>
      </g>
    </svg>

    <div class="title-box">
      <h1 class="event-name">Morvella!</h1>
    </div>

    <section class="info-band">
      <p class="tagline">Flavours of the Open Table</p>
      <div class="details">
        <span>Friday June 19th 2009</span>
        <span>Tollgate Plaza</span>
        <span>21.00 hrs - 01.00 hrs</span>
      </div>
      <p class="welcome">Everyone Welcome. Free Entry, Firework and Laser Display at 22.30 hrs</p>
      <p class="promoter">BrightLanternShows.com</p>
    </section>
  </main>
</body>
</html>
```